Business Card for Modern Marketing Consultancy

Business card needed for marketing consultancy with existing logo.

Lanternway Co is a specialized boutique marketing consultancy that provides startup, small and mid size consumer businesses thought leadership and implementation of marketing strategies to help your business grow.

Our expertise, experience and industry knowledge stems from some of New York’s top global beauty and retail companies and allows us to draw from an array of successful marketing strategies and growth tactics tailored to suit the needs of your business

lanternwayco.example

Target Market(s)

start up, small and mid size consumer packaged goods businesses

Industry/Entity Type

Leadership

Requirements
Must have
• Must have the logo of the business and use of the exact colors of the logo.
Must be simple, sleek, modern and clean. Must make a statement and be eye catching.

Front: looking for unique design or visual statement with logo and tagline

Back of card should have:
logo - if not use on front.
Delia R. Horvath
Founder
Lanternway Co
m: 555.014.2276
deliahorvath@lanternwayco.example
lanternwayco.example

Please use the following words as these describe my services:
strategy analytics branding research

Please refer to the website look and feel: lanternwayco.example

Please kindly note that I am looking for a unique design that I cannot do myself with a template. thank you.
Nice to have
• Please also try and incorporate additional files attached.

```html
<!DOCTYPE html>
<html lang="en">
<head>
<meta charset="utf-8">
<title>Lanternway Co — Business Card</title>
<link rel="stylesheet" href="https://fonts.googleapis.com/css2?family=Quicksand:wght@400;500;600;700&display=swap">
<style>
  :root {
    --backdrop: #ededed;
    --pink: #e4238a;
    --pink-deep: #b8135f;
    --pink-ink: #a8124f;
    --pink-soft: #f7c6df;
    --ink-grey: #66676b;
    --rule-grey: #b9b9bb;
    --paper: #ffffff;
    --card-w: 540px;
    --card-h: 308px;
  }
  * { box-sizing: border-box; margin: 0; padding: 0; }
  html, body {
    width: 1200px;
    height: 900px;
    overflow: hidden;
    background: var(--backdrop);
    font-family: "Quicksand", sans-serif;
  }
  .sheet {
    width: 1200px;
    height: 900px;
    display: flex;
    align-items: center;
    justify-content: center;
    gap: 40px;
  }
  .card {
    position: relative;
    width: var(--card-w);
    height: var(--card-h);
    overflow: hidden;
    box-shadow: 0 2px 10px rgba(0,0,0,0.12);
  }

  /* Front */
  .card-front {
    background: linear-gradient(90deg, var(--pink-deep) 0%, var(--pink) 70%, #ec2c93 100%);
    color: var(--paper);
  }
  .front-brand {
    position: absolute;
    left: 52px;
    top: 92px;
    display: flex;
    align-items: center;
    gap: 12px;
  }
  .front-brand .wordmark {
    font-size: 50px;
    font-weight: 600;
    letter-spacing: -0.5px;
    line-height: 1;
  }
  .front-brand .brand-dot {
    width: 14px;
    height: 14px;
    border-radius: 50%;
    background: var(--paper);
  }
  .front-tagline {
    position: absolute;
    left: 56px;
    top: 160px;
    font-size: 19px;
    font-weight: 500;
    letter-spacing: 0.8px;
    color: var(--pink-soft);
  }
  .services {
    position: absolute;
    left: 0;
    right: 0;
    bottom: 30px;
    display: flex;
    justify-content: center;
    align-items: center;
    gap: 20px;
    list-style: none;
    font-size: 17px;
    font-weight: 500;
    letter-spacing: 0.6px;
    color: #f7d4e6;
  }
  .services .sep {
    width: 8px;
    height: 8px;
    border-radius: 50%;
    background: var(--paper);
  }

  /* Back */
  .card-back {
    background: var(--paper);
    color: var(--ink-grey);
  }
  .back-brand {
    position: absolute;
    left: 0;
    right: 0;
    top: 30px;
    text-align: center;
  }
  .back-brand .wordmark {
    display: inline-flex;
    align-items: center;
    gap: 10px;
    font-size: 46px;
    font-weight: 600;
    letter-spacing: -0.5px;
    line-height: 1;
    color: var(--ink-grey);
  }
  .back-brand .brand-dot {
    width: 12px;
    height: 12px;
    border-radius: 50%;
    background: var(--pink-ink);
  }
  .back-tagline {
    margin-top: 6px;
    font-size: 16px;
    font-weight: 600;
    letter-spacing: 0.6px;
    color: var(--pink-ink);
  }
  .contact {
    position: absolute;
    left: 0;
    right: 0;
    top: 118px;
    text-align: center;
    font-style: normal;
    font-size: 15px;
    line-height: 1.2;
    letter-spacing: 0.8px;
  }
  .contact .person-name { font-size: 17px; }
  .contact .rule {
    width: 250px;
    margin: 6px auto;
    border-top: 1.5px dotted var(--rule-grey);
  }
  .contact .web { color: var(--pink-ink); }
  .edge-dots {
    position: absolute;
    left: 0;
    right: 0;
    bottom: 18px;
    display: flex;
    justify-content: space-around;
    padding: 0 30px;
  }
  .edge-dots span {
    width: 8px;
    height: 8px;
    border-radius: 50%;
    background: var(--pink-ink);
  }
</style>
</head>
<body>
<main class="sheet">

  <section class="card card-front" aria-label="Card front">
    <div class="front-brand">
      <span class="wordmark">Lanternway Co</span>
      <span class="brand-dot"></span>
    </div>
    <p class="front-tagline">Marketing With Clear Direction</p>
    <ul class="services">
      <li>strategy</li>
      <li class="sep" aria-hidden="true"></li>
      <li>analytics</li>
      <li class="sep" aria-hidden="true"></li>
      <li>branding</li>
      <li class="sep" aria-hidden="true"></li>
      <li>research</li>
    </ul>
  </section>

  <section class="card card-back" aria-label="Card back">
    <header class="back-brand">
      <span class="wordmark">Lanternway Co <span class="brand-dot"></span></span>
      <p class="back-tagline">marketing with clear direction</p>
    </header>
    <address class="contact">
      <p class="person-name">Delia R. Horvath</p>
      <p class="person-role">Founder</p>
      <div class="rule"></div>
      <p>Lanternway Co</p>
      <p>555.014.2276</p>
      <p>deliahorvath@lanternwayco.example</p>
      <div class="rule"></div>
      <p class="web">www.lanternwayco.example</p>
    </address>
    <div class="edge-dots" aria-hidden="true">
      <span></span><span></span><span></span><span></span><span></span>
    </div>
  </section>

</main>
</body>
</html>
```